Business Card Design

We need a business card designed which uses our logo and looks really good. The company is called LumaPivot482. We help e-commerce companies reduce cart abandonment by rescuing the sale through our innovative technology.

Our corporate colors are red, black and white.

I have attached our AI file for the logo as well.
Updates

Additional information for the business card:

Name: Derek Malloy
Title: President/CTO
Phone: 1-855-LUMA-482
Website: www.lumapivot482.com
Email: derek@lumapivot482.com

Tag line: Every Cart Reaches Checkout

Industry/Entity Type

E-Commerce

```html
<!DOCTYPE html>
<html lang="en">
<head>
<meta charset="utf-8">
<title>LumaPivot482 Business Card</title>
<link rel="stylesheet" href="https://fonts.googleapis.com/css2?family=Arimo:wght@400;700&family=Raleway:wght@400&display=swap">
<style>
  :root {
    --bg: #f2f2f2;
    --card: #ffffff;
    --ink: #111111;
    --logo-grey: #333333;
    --brand-red: #e0281f;
    --icon-blue: #2f7fd1;
    --shadow: rgba(0,0,0,0.14);
  }
  * { margin: 0; padding: 0; box-sizing: border-box; }
  html, body {
    width: 1200px; height: 882px; overflow: hidden;
    background: var(--bg);
  }
  .card {
    position: absolute; left: 100px; top: 155px;
    width: 1000px; height: 572px;
    background: var(--card);
    box-shadow: 0 10px 30px var(--shadow);
    font-family: "Arimo", Arial, sans-serif;
    color: var(--ink);
  }
  .brand {
    position: absolute; top: 92px; left: 0; right: 0;
    text-align: center;
  }
  .brand-name {
    display: inline-flex; align-items: center; gap: 16px;
    font-family: "Raleway", Arial, sans-serif;
    font-weight: 400; font-size: 62px; letter-spacing: 2px;
    color: var(--logo-grey); line-height: 1;
  }
  .brand-mark {
    width: 44px; height: 44px; background: var(--brand-red);
  }
  .tagline {
    margin-top: 14px;
    font-size: 22px; letter-spacing: 5px;
    color: var(--brand-red);
  }
  .person {
    position: absolute; left: 185px; top: 300px;
  }
  .person-name { font-weight: 700; font-size: 30px; }
  .person-title {
    margin-top: 4px; font-weight: 700; font-size: 22px;
    color: var(--brand-red);
  }
  .contacts {
    position: absolute; left: 520px; top: 262px;
    list-style: none;
  }
  .contact {
    display: flex; align-items: center; gap: 14px;
    font-weight: 700; font-size: 24px; height: 44px;
  }
  .contact svg { width: 30px; height: 30px; flex: none; }
</style>
</head>
<body>
  <section class="card">
    <header class="brand">
      <div class="brand-name"><span class="brand-mark"></span>LumaPivot482</div>
      <p class="tagline">Every Cart Reaches Checkout</p>
    </header>

    <div class="person">
      <p class="person-name">Derek Malloy</p>
      <p class="person-title">President/CTO</p>
    </div>

    <ul class="contacts">
      <li class="contact">
        <svg viewBox="0 0 30 30" aria-hidden="true">
          <circle cx="15" cy="15" r="14" fill="var(--icon-blue)"/>
          <path d="M10 8c-1 1-1.5 3 1 7s5 6.5 7 6.5c1 0 2-.8 2.5-1.5l-2.5-2.5-1.8 1c-1.5-.8-3.5-3-4.2-4.5l1-1.8L10.5 7.6z" fill="#fff"/>
        </svg>
        <span>1-855-LUMA-482</span>
      </li>
      <li class="contact">
        <svg viewBox="0 0 30 30" aria-hidden="true">
          <circle cx="15" cy="15" r="14" fill="var(--icon-blue)"/>
          <g fill="none" stroke="#fff" stroke-width="1.6">
            <circle cx="15" cy="15" r="9"/>
            <ellipse cx="15" cy="15" rx="4" ry="9"/>
            <line x1="6" y1="15" x2="24" y2="15"/>
          </g>
        </svg>
        <span>www.lumapivot482.com</span>
      </li>
      <li class="contact">
        <svg viewBox="0 0 30 30" aria-hidden="true">
          <rect x="2" y="7" width="26" height="18" rx="2" fill="var(--icon-blue)"/>
          <path d="M3 8l12 9 12-9" fill="none" stroke="#fff" stroke-width="1.8"/>
        </svg>
        <span>derek@lumapivot482.com</span>
      </li>
    </ul>
  </section>
</body>
</html>
```